Automotive eCommerce Business looking for a business card design

Looking for a clean and simple business card design. Our company name is "Harbor Crest Auto" and we are a company specializing in the ecommerce sales of automotive parts, specifically for pick up trucks and large SUVs. Our company colours are red, black, and white.

Feel free to use the logo provided or create a new logo that you seem fit. Looking forward to your creative ideas!

Industry/Entity Type

Automotive

Contact Information for Business Card

We were thinking of a possibly two-sided design featuring just the logo and company name on one side, and personal information on the other side. Single sided designs will be considered as well.

Font styles to use
Serif
Sans Serif
Decorative

Colors
ec1f27
ffffff
000000

Requirements
Must have
• Space for employee's name, title, phone number and email address, along with the company address and website somewhere.

```html
<!DOCTYPE html>
<html lang="en">
<head>
<meta charset="utf-8">
<title>Harbor Crest Auto — Business Card</title>
<link rel="stylesheet" href="https://fonts.googleapis.com/css2?family=Tinos&family=Questrial&display=swap">
<style>
  :root {
    --brand-red: #c11f2a;
    --ink: #111111;
    --paper: #ffffff;
    --backdrop: #e9e9ea;
    --mesh: #f1f1f3;
  }
  * { box-sizing: border-box; margin: 0; padding: 0; }
  html, body { width: 1200px; height: 1200px; overflow: hidden; background: var(--backdrop); }
  .canvas { position: relative; width: 1200px; height: 1200px; }
  .card {
    position: absolute; left: 150px; width: 900px; height: 514px;
    background: var(--paper); overflow: hidden;
    box-shadow: 0 10px 30px rgba(0,0,0,.12);
  }
  .card--front { top: 60px; }
  .card--back { top: 626px; }
  .card svg.shape { position: absolute; inset: 0; }
  .mesh-area { position: absolute; background: linear-gradient(120deg, var(--mesh), rgba(241,241,243,0)); }
  .front-mesh { left: 0; top: 0; width: 420px; height: 514px; }
  .back-mesh { left: 0; top: 0; width: 520px; height: 514px; }

  .front-brand { position: absolute; left: 300px; top: 150px; width: 520px; text-align: center; color: var(--paper); }
  .front-brand__name { font-family: "Tinos", serif; font-size: 46px; letter-spacing: 1px; }
  .front-brand__rule { width: 380px; height: 2px; background: var(--paper); margin: 14px auto 14px; }
  .front-brand__tagline { font-family: "Questrial", sans-serif; font-size: 22px; line-height: 1.3; }

  .back-brand { position: absolute; left: 50px; top: 70px; display: flex; align-items: center; gap: 18px; }
  .back-brand__mark { width: 44px; height: 44px; background: var(--brand-red); border-radius: 8px; }
  .back-brand__name { font-family: "Tinos", serif; font-size: 40px; color: var(--ink); }

  .person { position: absolute; right: 44px; top: 60px; text-align: right; color: var(--paper); font-family: "Questrial", sans-serif; }
  .person__name { font-size: 46px; letter-spacing: 1px; }
  .person__title { font-size: 22px; margin-top: 2px; }
  .person__rule { width: 110px; height: 4px; background: var(--paper); margin: 18px 0 0 auto; }

  .contact { position: absolute; right: 44px; top: 290px; list-style: none; color: var(--paper); font-family: "Questrial", sans-serif; font-size: 22px; text-align: right; }
  .contact li { display: flex; justify-content: flex-end; align-items: flex-start; gap: 12px; line-height: 32px; }
  .contact svg { width: 20px; height: 20px; margin-top: 6px; flex: none; }
</style>
</head>
<body>
<main class="canvas">

  <section class="card card--front" aria-label="Business card front">
    <div class="mesh-area front-mesh" role="img" aria-label="Faint network line pattern"></div>
    <svg class="shape" width="900" height="514" viewBox="0 0 900 514">
      <polygon points="400,50 720,50 800,257 720,464 400,464 320,257" fill="var(--brand-red)" stroke="var(--brand-red)" stroke-width="70" stroke-linejoin="round"/>
    </svg>
    <div class="front-brand">
      <div class="front-brand__name">Harbor Crest Auto Ltd.</div>
      <div class="front-brand__rule"></div>
      <p class="front-brand__tagline">Specializing in The E-commerce<br>Sales of Automotive Parts</p>
    </div>
  </section>

  <section class="card card--back" aria-label="Business card back">
    <div class="mesh-area back-mesh" role="img" aria-label="Faint network line pattern"></div>
    <svg class="shape" width="900" height="514" viewBox="0 0 900 514">
      <path d="M585 -10 L440 170 Q425 190 425 215 L425 530" fill="none" stroke="var(--ink)" stroke-width="4"/>
      <path d="M605 0 L900 0 L900 514 L445 514 L445 220 Q445 195 460 176 Z" fill="var(--brand-red)"/>
    </svg>
    <div class="back-brand">
      <span class="back-brand__mark"></span>
      <span class="back-brand__name">Harbor Crest Auto Ltd.</span>
    </div>
    <div class="person">
      <div class="person__name">Daniel Reyes</div>
      <div class="person__title">Managing Director</div>
      <div class="person__rule"></div>
    </div>
    <ul class="contact">
      <li>555.012.3480
        <svg viewBox="0 0 24 24" fill="#fff"><path d="M6.6 10.8a15.1 15.1 0 0 0 6.6 6.6l2.2-2.2a1 1 0 0 1 1-.25 11.4 11.4 0 0 0 3.6.6 1 1 0 0 1 1 1V20a1 1 0 0 1-1 1A17 17 0 0 1 3 4a1 1 0 0 1 1-1h3.5a1 1 0 0 1 1 1c0 1.25.2 2.45.57 3.57a1 1 0 0 1-.25 1z"/></svg></li>
      <li>info@harborcrestauto.com
        <svg viewBox="0 0 24 24" fill="none" stroke="#fff" stroke-width="2"><rect x="3" y="5" width="18" height="14" rx="2"/><path d="M3 7l9 6 9-6"/></svg></li>
      <li>www.harborcrestauto.com
        <svg viewBox="0 0 24 24" fill="none" stroke="#fff" stroke-width="2"><circle cx="12" cy="12" r="9"/><path d="M3 12h18M12 3c3 3 3 15 0 18M12 3c-3 3-3 15 0 18"/></svg></li>
      <li>48 Linden Avenue,<br>Portland, USA
        <svg viewBox="0 0 24 24" fill="#fff"><path d="M12 3l9 8h-3v9h-4v-6h-4v6H6v-9H3z"/></svg></li>
    </ul>
  </section>

</main>
</body>
</html>
```